Business Card Design Project

I am looking for a minimal matte background/shiny (spot UV) ink monochromatic design with a splash of neon color.

the card should be 2 sided, logo only on one side - all info and possibly logo on the other.

My creative director described the colors he imagined for the design to be:
'it's a dark field, like charcoal or a really dark burgundy, or deep blue, shot through with a neon—but just a tiny bit of it. so a charcoal field with a laser-thin streak of electric lime, safety orange, or cobalt blue. really beautiful stuff.'

here are some samples of the types of cards I am trying to create:
http://www.pictavault.example/photos/dawnpress/6967376935/in/photostream -> Vandrelle Lustre

http://www.pictavault.example/photos/dawnpress/6497659409/in/photostream -> Standard Coated (14pt/matte) with SPOT UV

http://www.pictavault.example/photos/dawnpress/6497658995/in/photostream/ -> Heavy Corvane with Raised Ink

http://www.pictavault.example/photos/dawnpress/6275629165/in/photostream/ -> Standard Coated (14pt/matte) with SPOT UV

Here is my logo:
https://www.filecrate.example/s/sigym192mlh58ge/quillorb%20logotype%20final.ai

Here are the details for info:
Dorian Elwood Marsh
email - dorian@quillorb.example
mobile - 555 013 2867
web -
quillorb.example: inventive technology applications
quillorb-tv.example: innovative video advertising

please let me know if there is anything at all that you need.

Target Market(s)

mid to large agencies that require interactive design and entrepreneurial/startup individuals/companies that need application development.

Industry/Entity Type

Safety

Requirements
Must have
• logo only on one side

```html
<!DOCTYPE html>
<html lang="en">
<head>
<meta charset="utf-8">
<title>Quillorb Business Card</title>
<link rel="stylesheet" href="https://fonts.googleapis.com/css2?family=Questrial&display=swap">
<style>
  :root {
    --backdrop: #1d1d1f;
    --band-dark: #525254;
    --band-darker: #48484a;
    --band-light: #9d9d9f;
    --ink-dark: #2a2a2c;
    --ink-light: #f2f2f2;
    --pill-fill: #141416;
    --pill-edge: #8a8a8c;
    --card-edge: #6a6a6c;
    --neon-lime: #c6ff1a;
  }
  * { margin: 0; padding: 0; box-sizing: border-box; }
  html, body {
    width: 1200px;
    height: 842px;
    overflow: hidden;
    background: var(--backdrop);
    font-family: "Questrial", sans-serif;
  }
  .sheet {
    position: relative;
    width: 1200px;
    height: 842px;
    display: flex;
    align-items: center;
    justify-content: center;
    gap: 40px;
  }
  .card {
    position: relative;
    width: 540px;
    height: 309px;
    background: var(--band-dark);
    border: 1px solid var(--card-edge);
    overflow: hidden;
  }
  .band { position: absolute; left: 0; width: 100%; }
  .neon-streak {
    position: absolute; left: 0; width: 100%; height: 2px;
    background: var(--neon-lime);
    box-shadow: 0 0 6px var(--neon-lime);
  }

  /* Front: logo only */
  .card--front .band--top { top: 0; height: 96px; background: var(--band-dark); }
  .card--front .band--middle {
    top: 96px; height: 110px; background: var(--band-light);
    display: flex; align-items: center; justify-content: center;
  }
  .card--front .band--bottom { top: 206px; height: 103px; background: var(--band-dark); }
  .card--front .neon-streak { top: 206px; }
  .wordmark {
    display: flex; align-items: center; gap: 22px;
    color: var(--ink-dark);
  }
  .wordmark__name {
    font-size: 54px;
    letter-spacing: 16px;
    line-height: 1;
  }
  .wordmark__square {
    width: 18px; height: 18px; background: var(--ink-dark);
  }

  /* Back: contact details */
  .card--back .band--top { top: 0; height: 100px; background: var(--band-dark); }
  .card--back .band--middle {
    top: 100px; height: 86px; background: var(--band-light);
    display: flex; align-items: center; justify-content: space-between;
    padding: 0 30px;
  }
  .card--back .band--bottom { top: 186px; height: 123px; background: var(--band-darker); }
  .card--back .neon-streak { top: 186px; }
  .brand-tag {
    width: 96px;
    font-size: 14px;
    letter-spacing: 3px;
    color: var(--ink-dark);
  }
  .brand-tag--right { text-align: right; }
  .contact-person { text-align: center; color: var(--ink-light); }
  .contact-person__name { font-size: 21px; letter-spacing: 1px; line-height: 1.1; }
  .contact-person__phone { font-size: 16px; letter-spacing: 2px; }

  .links {
    position: absolute; left: 0; top: 232px; width: 100%;
    display: flex; justify-content: space-around; padding: 0 10px;
  }
  .link-pill { position: relative; width: 164px; height: 32px; }
  .link-pill svg { position: absolute; inset: 0; }
  .link-pill__text {
    position: absolute; inset: 0;
    display: flex; align-items: center; justify-content: center;
    color: var(--ink-light); font-size: 10.5px; letter-spacing: 0.4px;
    white-space: nowrap;
  }
</style>
</head>
<body>
<main class="sheet">
  <section class="card card--front" aria-label="Card front">
    <div class="band band--top"></div>
    <div class="band band--middle">
      <div class="wordmark">
        <span class="wordmark__name">QUILLORB</span>
        <span class="wordmark__square"></span>
      </div>
    </div>
    <div class="band band--bottom"></div>
    <div class="neon-streak"></div>
  </section>

  <section class="card card--back" aria-label="Card back">
    <div class="band band--top"></div>
    <div class="band band--middle">
      <span class="brand-tag">QUILLORB</span>
      <div class="contact-person">
        <p class="contact-person__name">Dorian Elwood Marsh</p>
        <p class="contact-person__phone">555 013 2867</p>
      </div>
      <span class="brand-tag brand-tag--right">QUILLORB</span>
    </div>
    <div class="band band--bottom"></div>
    <div class="neon-streak"></div>

    <div class="links">
      <div class="link-pill">
        <svg width="164" height="32" viewBox="0 0 164 32"><polygon points="14,1 150,1 163,16 150,31 14,31 1,16" fill="var(--pill-fill)" stroke="var(--pill-edge)" stroke-width="1"/></svg>
        <span class="link-pill__text">www.quillorb.example</span>
      </div>
      <div class="link-pill">
        <svg width="164" height="32" viewBox="0 0 164 32"><polygon points="14,1 150,1 163,16 150,31 14,31 1,16" fill="var(--pill-fill)" stroke="var(--pill-edge)" stroke-width="1"/></svg>
        <span class="link-pill__text">dorian@quillorb.example</span>
      </div>
      <div class="link-pill">
        <svg width="164" height="32" viewBox="0 0 164 32"><polygon points="14,1 150,1 163,16 150,31 14,31 1,16" fill="var(--pill-fill)" stroke="var(--pill-edge)" stroke-width="1"/></svg>
        <span class="link-pill__text">www.quillorb-tv.example</span>
      </div>
    </div>
  </section>
</main>
</body>
</html>
```